Letter Head for Gay Brand

A new letterhead is required for a Gay Bar Brand in Central London.

The letter head must include the following:
- The 3 venue addresses
- Company Name and Head Office address with registered company details including VAT number as on the current letterhead.
- Websites: www.vex-lounge.com and www.mira-dean.com

Addresses:
- Head Office:
Brindle Ventures Ltd. 14 Carver Lane, London WC2E 9PQ, T: 0207 318 6952,
E: info@vex-lounge.co.uk
- Vex Marden Sq. / VexVault, 14 Carver Lane, London WC2E 9PQ, T: 0207 318 6952
E: info@vex-lounge.co.uk
- Vex Dean, 41 Harrow Row, London W1F 8TN, T: 0207 318 6952,
E: info@vex-lounge.co.uk
- Mira Dean, 17b New Barnaby Street, London W1F 8TN, T: 0207 318 6952
E: info@mira-dean.com

The 3 logos must be visible in some way that work well together. We'd like to keep a similar effect on the back of the letterhead, colour and logos to make a bold impact.

Looking for something bold and contemporary but not to distract too much when using as a letter. Soemthing that we can also use as a basis for business cards too.

I have also attached suitable logos for you to use.

```html
<!DOCTYPE html>
<html lang="en">
<head>
<meta charset="utf-8">
<title>Brindle Ventures Ltd. – Letterhead</title>
<link rel="stylesheet" href="https://fonts.googleapis.com/css2?family=Jost:wght@400;600;800&display=swap">
<style>
  :root {
    --backdrop: #8a8a8a;
    --paper: #ffffff;
    --ink: #1a1a1a;
    --ink-soft: #3a3a3a;
    --bar-top: #b89a68;
    --bar-bottom: #f2d400;
  }
  * { box-sizing: border-box; margin: 0; padding: 0; }
  html, body {
    width: 1200px;
    height: 1000px;
    overflow: hidden;
    background: var(--backdrop);
    font-family: "Jost", sans-serif;
    color: var(--ink);
  }
  .letterhead {
    position: absolute;
    left: 275px;
    top: 40px;
    width: 650px;
    height: 920px;
    background: var(--paper);
    box-shadow: 0 6px 18px rgba(0,0,0,0.25);
  }
  .footer {
    position: absolute;
    left: 0;
    right: 0;
    bottom: 56px;
    text-align: center;
  }
  .venues {
    display: flex;
    justify-content: center;
    align-items: flex-end;
    gap: 26px;
    margin-bottom: 10px;
  }
  .venue {
    width: 140px;
    text-align: center;
    font-size: 9.5px;
    line-height: 1.3;
    color: var(--ink-soft);
  }
  .venue-name {
    display: block;
    font-weight: 800;
    color: var(--ink);
    line-height: 1;
    margin-bottom: 6px;
    white-space: nowrap;
  }
  .venue-name--large { font-size: 24px; letter-spacing: -0.5px; }
  .venue-name--medium { font-size: 20px; }
  .venue-name--small { font-size: 16px; letter-spacing: 1px; }
  .venue-title {
    font-weight: 600;
    color: var(--ink);
  }
  .divider {
    width: 4px;
    height: 78px;
    background: linear-gradient(to bottom, var(--bar-top), var(--bar-bottom));
  }
  .head-office-title {
    font-size: 11px;
    font-weight: 800;
    letter-spacing: 0.5px;
    margin-bottom: 3px;
  }
  .head-office-line {
    font-size: 9.5px;
    line-height: 1.45;
    color: var(--ink-soft);
  }
  .company-name {
    font-weight: 600;
    color: var(--ink);
  }
</style>
</head>
<body>
  <main class="letterhead">
    <footer class="footer">
      <div class="venues">
        <div class="venue">
          <span class="venue-name venue-name--large">VexVault</span>
          <span class="venue-title">Vex Marden Sq. / VexVault</span><br>
          14 Carver Lane<br>
          London WC2E 9PQ<br>
          T: 0207 318 6952<br>
          E: info@vex-lounge.co.uk
        </div>
        <div class="divider"></div>
        <div class="venue">
          <span class="venue-name venue-name--medium">Vex Dean</span>
          <span class="venue-title">Vex Dean</span><br>
          41 Harrow Row<br>
          London W1F 8TN<br>
          T: 0207 318 6952<br>
          E: info@vex-lounge.co.uk
        </div>
        <div class="divider"></div>
        <div class="venue">
          <span class="venue-name venue-name--small">MIRA DEAN</span>
          <span class="venue-title">Mira Dean</span><br>
          17b New Barnaby Street<br>
          London W1F 8TN<br>
          T: 0207 318 6952<br>
          E: info@mira-dean.com
        </div>
      </div>
      <div class="head-office">
        <p class="head-office-title">HEAD OFFICE</p>
        <p class="head-office-line"><span class="company-name">Brindle Ventures Ltd.</span> | 14 Carver Lane | London WC2E 9PQ | T: 0207 318 6952 | E: info@vex-lounge.co.uk</p>
        <p class="head-office-line">Registered in England: 04815267 | VAT Number: 612 483 907</p>
        <p class="head-office-line">www.vex-lounge.com | www.mira-dean.com</p>
      </div>
    </footer>
  </main>
</body>
</html>
```